design a catchy flyer for my electrical buisness

need a flyer designed to attract people to my business by looking professional and offering specials

Target Market(s)

all people i want to look affordable to everyone but still keeping that professional look and feel

Industry/Entity Type

Electrical

Requirements
Must have
• NO JOB TO BIG OR SMALL
• CALL NOW FOR A FREE QUOTE 0400318726
• NO CALL OUT FEE
• same promises as uploaded pic maybe written different style
• Your neighborhood electrician
• 100% satisfaction guaranteed
• were here to help
• mention this flyer for 10% off
• specializing in house renovations, extensions, kitchen and bathroom upgrades switchboard upgrades
• Make your house safe with our RCD and smoke alarm packages
Nice to have
• modern
• proffesional
• shows trust when customers read it
Should not have
• corny slogans
• cheap look

```html
<!DOCTYPE html>
<html lang="en">
<head>
<meta charset="utf-8">
<title>Neighborhood Electrician Flyer</title>
<link href="https://fonts.googleapis.com/css2?family=Roboto+Condensed:wght@300;400;700;800&family=Roboto:wght@500;700&display=swap" rel="stylesheet">
<style>
  :root{
    --stage:#2b2f36;
    --paper:#ffffff;
    --panel:#dcdcdd;
    --red:#d0141c;
    --red-dark:#b8121a;
    --orange:#f4891f;
    --yellow:#fff200;
    --ink:#1a1a1a;
    --muted:#555;
    --tick:#5a5a5a;
  }
  *{box-sizing:border-box;margin:0;padding:0}
  html,body{width:1200px;height:1200px;overflow:hidden;background:var(--stage)}
  body{position:relative;font-family:"Roboto Condensed",Arial,sans-serif;color:var(--ink)}
  .flyer{position:absolute;left:235px;top:36px;width:812px;height:1254px;background:var(--paper);
    transform:scale(0.9);transform-origin:0 0;overflow:hidden}
  .abs{position:absolute}
  .panel{background:var(--panel)}
  .panel--main{left:33px;top:0;width:516px;height:1207px}
  .panel--foot{left:33px;top:1222px;width:516px;height:32px}
  .orange-col{background:var(--orange)}
  .orange-col--main{left:561px;top:558px;width:233px;height:649px}
  .orange-col--foot{left:561px;top:1222px;width:233px;height:32px}
  .hero-band{left:0;top:160px;width:606px;height:273px;background:linear-gradient(90deg,var(--red-dark),var(--red));}
  .hero-photo{left:530px;top:0;width:282px;height:560px;
    background:linear-gradient(180deg,#e9e4df 0%,#9fb0d8 35%,#3b56b8 60%,#a9adb5 100%);
    clip-path:polygon(18% 40%,30% 6%,70% 0,100% 4%,100% 100%,25% 100%,12% 82%)}
  .hero-tag{left:0;width:540px;top:180px;text-align:center;color:#fff;font-weight:700;font-size:28px}
  .hero-sub{left:0;width:550px;top:236px;text-align:center;color:#fff;font-weight:400;font-size:64px;letter-spacing:-1px}
  .hero-title{left:0;width:550px;top:314px;text-align:center;color:#fff;font-weight:800;font-size:92px;letter-spacing:-1px}
  .promise-head{left:52px;top:463px;font-weight:700;font-size:23px}
  .promises{left:46px;top:512px;width:470px;list-style:none;font-size:19px;line-height:24px}
  .promises li{position:relative;padding-left:30px;margin-bottom:11px}
  .promises svg{position:absolute;left:0;top:5px}
  .specials{left:0;top:896px;width:561px;height:136px;background:var(--yellow)}
  .specials ul{position:absolute;left:76px;top:14px;width:420px;font-size:16.5px;line-height:22px;list-style:none}
  .specials li{position:relative;padding-left:20px;margin-bottom:15px}
  .specials li::before{content:"";position:absolute;left:0;top:9px;width:5px;height:5px;border-radius:50%;background:var(--ink)}
  .brand-dot{left:134px;top:1080px;width:74px;height:74px;border-radius:50%;border:6px solid var(--muted)}
  .brand-name{left:242px;top:1096px;font-family:"Roboto",sans-serif;font-weight:500;font-size:34px;color:var(--orange)}
  .brand-phone{left:245px;top:1150px;font-family:"Roboto",sans-serif;font-weight:700;font-size:28px;letter-spacing:1px}
  .badge{left:560px;top:508px;width:230px;height:230px}
  .cta{left:561px;width:233px;text-align:center}
  .cta--call{top:753px;color:#fff;font-weight:300;font-size:34px;line-height:42px}
  .cta--free{top:837px;color:var(--red);font-weight:400;font-size:35px}
  .cta--num{top:886px;font-weight:800;font-size:56px;line-height:62px;color:#000}
  .offer{left:561px;top:1030px;width:233px;height:170px}
</style>
</head>
<body>
<main class="flyer">
  <div class="abs panel panel--main"></div>
  <div class="abs panel panel--foot"></div>
  <div class="abs orange-col orange-col--main"></div>
  <div class="abs orange-col orange-col--foot"></div>

  <div class="abs hero-band"></div>
  <div class="abs hero-photo" role="img" aria-label="Photo of a smiling electrician in blue overalls carrying a coil of cable and a tool belt"></div>
  <p class="abs hero-tag">were here to help</p>
  <h1 class="abs hero-sub">Your Neighborhood</h1>
  <h2 class="abs hero-title">Electrician</h2>

  <h3 class="abs promise-head">NO JOB TO BIG OR SMALL</h3>
  <ul class="abs promises">
    <li><svg width="16" height="14" viewBox="0 0 16 14"><path d="M1 7l5 5L15 2" fill="none" stroke="var(--tick)" stroke-width="3.5"/></svg>We will provide you with a fixed price<br>gurantee assuring no extra costs</li>
    <li><svg width="16" height="14" viewBox="0 0 16 14"><path d="M1 7l5 5L15 2" fill="none" stroke="var(--tick)" stroke-width="3.5"/></svg>We will leave your place as clean as when we arrived</li>
    <li><svg width="16" height="14" viewBox="0 0 16 14"><path d="M1 7l5 5L15 2" fill="none" stroke="var(--tick)" stroke-width="3.5"/></svg>We will rovide a 12 Month warranty on all parts</li>
    <li><svg width="16" height="14" viewBox="0 0 16 14"><path d="M1 7l5 5L15 2" fill="none" stroke="var(--tick)" stroke-width="3.5"/></svg>We will provide friendly, helpful service and advice</li>
    <li><svg width="16" height="14" viewBox="0 0 16 14"><path d="M1 7l5 5L15 2" fill="none" stroke="var(--tick)" stroke-width="3.5"/></svg>We will arrive on time or we will pay you $100</li>
    <li><svg width="16" height="14" viewBox="0 0 16 14"><path d="M1 7l5 5L15 2" fill="none" stroke="var(--tick)" stroke-width="3.5"/></svg>Before any job begins you will know the exat cost</li>
    <li><svg width="16" height="14" viewBox="0 0 16 14"><path d="M1 7l5 5L15 2" fill="none" stroke="var(--tick)" stroke-width="3.5"/></svg>If there is a problem and it’s our fault<br>we will fix it for free</li>
    <li><svg width="16" height="14" viewBox="0 0 16 14"><path d="M1 7l5 5L15 2" fill="none" stroke="var(--tick)" stroke-width="3.5"/></svg>We will return your telephone calls promptly</li>
    <li><svg width="16" height="14" viewBox="0 0 16 14"><path d="M1 7l5 5L15 2" fill="none" stroke="var(--tick)" stroke-width="3.5"/></svg>No Call Out Fee</li>
  </ul>

  <section class="abs specials">
    <ul>
      <li>Specializing in house renovations, extensions, kitchen<br>and bathroom upgrades, Switchboard upgrades.</li>
      <li>Make your house safe with our <b>RCD and<br>smoke alarm packages.</b></li>
    </ul>
  </section>

  <div class="abs brand-dot"></div>
  <p class="abs brand-name">VoltLine</p>
  <p class="abs brand-phone">0400 318 726</p>

  <svg class="abs badge" viewBox="0 0 230 230" aria-label="100% satisfaction guaranteed">
    <polygon fill="var(--red)" points="115,5 133,28 160,14 167,43 197,41 192,70 220,82 204,107 225,129 198,142 207,171 177,172 170,201 143,190 126,216 106,196 80,213 70,185 40,191 42,161 13,151 28,125 6,105 32,88 22,60 52,58 55,29 83,38 97,11"/>
    <g transform="rotate(6 115 115)" fill="#fff" font-family="Roboto Condensed, sans-serif" font-weight="800" text-anchor="middle">
      <text x="115" y="96" font-size="52" font-style="italic">100%</text>
      <text x="115" y="132" font-size="27">satisfaction</text>
      <text x="112" y="165" font-size="27">guaranteed</text>
    </g>
  </svg>

  <p class="abs cta cta--call">CALL NOW<br>FOR A</p>
  <p class="abs cta cta--free">FREE QUOTE</p>
  <p class="abs cta cta--num">0400<br>318 726</p>

  <svg class="abs offer" viewBox="0 0 233 170" aria-label="10% off">
    <path d="M10 120 C-5 60 60 28 130 30 C185 32 225 60 228 95 C232 140 180 168 110 160 C70 156 40 145 30 130" fill="none" stroke="#fff" stroke-width="5"/>
    <text x="116" y="110" text-anchor="middle" fill="#fff" font-family="Roboto Condensed, sans-serif" font-size="54"><tspan font-weight="800">10%</tspan> off</text>
  </svg>
</main>
</body>
</html>
```